Book Cover Design Project

I need a book cover for a book that we will be releasing in the next few months.

It is a business book aimed at small businesses and people who want to escape the 9 - 5 and start their own business.

We want it to look similar to: http://www.tolvanbrook.example/wp-content/uploads/2010/03/fold-up.jpg and also the book designs that I have uploaded images for.

I quite like the grey / charcoal background and the bright lime green colours from the Quiet Harbor logo that I have attached. However, anything bright would be good - I am prepared to be flexible with colours. The books I have attached are a high impact as well - being bright blue with white black font with a really cool font.

The book is titled:

The Lantern Shop Plan

By Dale Vortan

Still thinking of the tagline, for now just use "Start an Online Business in no time at all"

Room for a quote/testimonial on the front of the book at the bottom, and as well on the back.

For the back cover text just use dummy text and my photo that is attached for now as well.

Barcode ISBN on the back at the bottom - price will be $19.95

Needs to be in PSD so we can change the text from our end.

I really want to get a good template made that I can edit the text for as we are still developing the book, but I want to get the book cover done so I can start advertising that it will be arriving soon.

There will probably be alterations that I need help with later down the track so looking to work with someone closely on this, and I will pay you for any extra time down the track..

Sizes will probably be around: I think 20.5cm tall and 14cm wide would be good..

Not sure how thick for the spine, it will depend on how many words get cut off, but as an estimate probably 1.5CM..
Updates

Just added some more detail to the brief.. Please read it carefully.

Target Market(s)

small business owners, professionals who want to start their own business, soon to be entrepreneurs, entrepreneurs

Industry/Entity Type

Advertising

Requirements
Must have
• The Lantern Shop Plan

and Dale Vortan must be prominent.

Tag line should be look cool under the title.

Must be very modern and cool. Needs to catch people's eyes so needs to be really punchy.

Nice to have
• Maybe a clock or stopwatch icon would be cool to add in there so it isn't just plain.. Similar to like how the books have a cool icon with them that I have attached in the uploaded images.
Should not have
• I like simplicity, artistic and very high impact. It really needs to draw you in and catch your eye.

Don't use plain boring fonts. Although I like simplicity slick design is very important - I dont want it to be boring - it has to look high quality and expensive. Therefore do not use fonts like Arial, Times New Roman those really boring fonts that make it look cheap. If I was going to do something like that then I might as well do it myself.

If you want to see the quality of things that I am usually involved with look at the artwork for one of my events that I run called Daybreaker: http://www.daybreaker.example/daybreaker-festival-anthems-ft-loomsparrow-harvest-night-eve-metro-report/

That will give you an idea of what type of quality things that I am involved with, so you need to be up for the task..

```html
<!DOCTYPE html>
<html lang="en">
<head>
<meta charset="utf-8">
<title>The Lantern Shop Plan — Dale Vortan</title>
<link href="https://fonts.googleapis.com/css2?family=Oswald:wght@500;600;700&display=swap" rel="stylesheet">
<style>
  :root {
    --stage: #2a2a2a;
    --cover: #141414;
    --cover-edge: #1d1d1d;
    --lime: #f4e600;
    --white: #f4f4f4;
  }
  * { margin: 0; padding: 0; box-sizing: border-box; }
  html, body {
    width: 1200px;
    height: 920px;
    overflow: hidden;
    background: var(--stage);
  }
  .canvas {
    width: 1200px;
    height: 920px;
    display: flex;
    align-items: center;
    justify-content: center;
  }
  .cover {
    width: 600px;
    height: 840px;
    background: radial-gradient(ellipse at 40% 30%, var(--cover-edge), var(--cover) 70%);
    padding: 36px 52px 48px;
    display: flex;
    flex-direction: column;
    justify-content: space-between;
    font-family: "Oswald", "Arial Narrow", sans-serif;
    color: var(--lime);
  }
  .author {
    text-align: center;
    color: var(--white);
    font-weight: 600;
    font-size: 30px;
    letter-spacing: 3px;
    line-height: 1;
  }
  .rule {
    height: 4px;
    background: var(--white);
    margin: 14px auto 0;
    width: 82%;
  }
  .title {
    text-transform: uppercase;
    text-align: center;
    font-weight: 700;
  }
  .title-the {
    display: block;
    font-size: 64px;
    line-height: 1;
    letter-spacing: 2px;
  }
  .title-main {
    display: block;
    font-size: 136px;
    line-height: 1.02;
    letter-spacing: 1px;
    margin-top: 6px;
  }
  .title-sub {
    display: block;
    font-size: 120px;
    line-height: 1.02;
    letter-spacing: 2px;
  }
  .tagline-block .rule { width: 100%; margin: 0; }
  .tagline {
    text-align: center;
    color: var(--white);
    font-weight: 500;
    font-size: 20px;
    letter-spacing: 1.5px;
    text-transform: uppercase;
    padding: 12px 0;
  }
</style>
</head>
<body>
<main class="canvas">
  <article class="cover">
    <header>
      <p class="author">DALE VORTAN</p>
      <div class="rule"></div>
    </header>

    <h1 class="title">
      <span class="title-the">The</span>
      <span class="title-main">Lantern</span>
      <span class="title-sub">Shop</span>
      <span class="title-sub">Plan</span>
    </h1>

    <footer class="tagline-block">
      <div class="rule"></div>
      <p class="tagline">Start an online business in no time at all</p>
      <div class="rule"></div>
    </footer>
  </article>
</main>
</body>
</html>
```